Microsoft Word Template for 1, 2, and 4-page quick hit, topical pieces

I am looking for someone to create a professional and dynamic Microsoft Word Template that will allow us to easily add content to produce brochures and whitepapers on various topics. We'd like the template to be 4 pages with the idea that we may use all or just 1-2 of the pages in a brochure. We are fond of bold color, white space, and a good ratio of text to graphics. We have a large catalog of stock images so placeholders for photographs can be included if it fits the design. There is the possibility of expanded design opportunities in the future. I have attached our logo and colors.

Target Market(s)

Libraries - Public, Government, Higher Education, and Corporate

Font styles to use
Serif
Sans Serif

Requirements
Must have
• Editable Word Template that has 4 variable but cohesively designed pages. Use our logo and colors (see uploaded documents)
Nice to have
• Lots of white space, spaces for photos and graphics, spaces for blocks of text. Color.
Should not have
• Giant blocks of text. The exact same frame (header and footer) on each page.

```html
<!DOCTYPE html>
<html lang="en">
<head>
<meta charset="utf-8">
<title>Bellwick Brochure Template – Four Pages</title>
<link rel="stylesheet" href="https://fonts.googleapis.com/css2?family=Montserrat:wght@300;400;500;600;700;800&display=swap">
<style>
:root{
  --brown:#7a4208;
  --brown-soft:rgba(122,66,8,.88);
  --teal:#0f7585;
  --ink:#333;
  --paper:#fff;
  --stage:#f2f2f2;
}
*{margin:0;padding:0;box-sizing:border-box}
html,body{width:1200px;height:2755px;overflow:hidden}
body{background:var(--stage);font-family:"Montserrat",sans-serif;color:var(--ink);position:relative}
.slot{position:absolute;width:551px;height:717px}
.slot--tl{left:32px;top:640px}.slot--tr{left:617px;top:640px}
.slot--bl{left:32px;top:1397px}.slot--br{left:617px;top:1397px}
.page{position:absolute;left:0;top:0;width:492px;height:640px;background:var(--paper);transform:scale(1.12);transform-origin:0 0;box-shadow:0 2px 8px rgba(0,0,0,.12);overflow:hidden}
.abs{position:absolute}
.photo{position:absolute}
.photo--desk{background:linear-gradient(135deg,#e9e6e1 0%,#b9b4ad 45%,#5d5852 75%,#2f3a4d 100%)}
.photo--coder{background:linear-gradient(160deg,#2b3446 0%,#1b2130 45%,#b8a89a 80%,#e2d9cf 100%)}
.photo--office{background:linear-gradient(135deg,#f1efec 0%,#cfcac4 45%,#3a3a3a 75%,#9c9790 100%)}
.photo--cafe{background:linear-gradient(135deg,#cfd4d8 0%,#9aa0a6 40%,#3c3f46 70%,#1f2228 100%)}
.photo--laptop{background:linear-gradient(150deg,#f4f4f4 0%,#cfcfcf 50%,#2a2a2a 80%,#e6e6e6 100%)}
.body-text{font-size:8px;line-height:1.3;color:var(--ink)}
.body-text p+p{margin-top:7px}
.body-text--compact{font-size:7.6px;line-height:1.28;letter-spacing:-.05px}
.header{display:flex;align-items:center;gap:11px;font-weight:700;font-size:16px;color:var(--brown)}
.header::before{content:"";width:20px;height:20px;background:var(--brown)}
.teal-label{color:var(--teal);font-weight:700}
.brand{display:flex;align-items:center;gap:10px;font-weight:300;color:var(--brown);font-size:34px;letter-spacing:-.5px}
.brand__dot{width:36px;height:36px;border-radius:50%;background:#b59a2a}
/* cover */
.cover__frame{left:40px;top:90px;width:420px;height:238px;border:5px solid var(--brown)}
.cover__band{left:0;top:188px;width:385px;height:167px;background:var(--brown)}
.cover__title{left:52px;top:357px;font-size:29px;font-weight:800;color:var(--brown);letter-spacing:.3px}
.cover__subtitle{left:52px;top:392px;font-size:20px;font-weight:400;color:var(--brown);letter-spacing:.5px}
.cover__bar{left:0;bottom:0;width:100%;height:13px;background:var(--teal)}
/* inside page A */
.side__title{font-size:10px}
.side__list{list-style:none;font-size:8px;line-height:1.45}
.side__list li::before{content:"» ";font-weight:700;margin-right:8px}
.side__box{border:2px solid var(--teal);padding:5px 6px;color:var(--teal);font-size:7.3px;line-height:1.27;letter-spacing:-.05px;overflow:hidden}
.side__box p+p{margin-top:5px}
.photo__caption{position:absolute;left:0;bottom:0;width:100%;height:30px;background:rgba(15,117,133,.92);color:#fff;font-size:7.8px;text-align:center;line-height:1.25;padding-top:5px}
.thumb{position:absolute;width:86px}
.thumb__label{font-size:8.6px;margin-bottom:6px;display:block}
.thumb__img{height:86px}
.thumb__caption{font-size:8px;line-height:1.25;margin-top:8px}
.rule{position:absolute;height:1.5px;background:var(--teal)}
/* inside page B */
.step{position:absolute;width:198px}
.step__num{width:34px;height:34px;border-radius:50%;background:var(--teal);color:#fff;font-weight:600;font-size:14px;display:flex;align-items:center;justify-content:center}
.step__head{font-size:8.6px;margin-top:5px;padding:0 0 2px 2px;border-bottom:1.5px solid var(--teal)}
.step .body-text{margin-top:7px;padding-left:2px}
/* back */
.back__band{left:0;top:185px;width:100%;height:170px;background:var(--brown-soft)}
.back__title{left:0;top:250px;width:100%;text-align:center;font-size:28px;font-weight:800;color:#fff;letter-spacing:.3px}
.contact{list-style:none;font-size:8px;color:var(--brown);line-height:1.95}
.contact li{display:flex;align-items:center;gap:8px}
.contact svg{width:10px;height:10px;flex:none}
</style>
</head>
<body>

<!-- Page 1 : cover -->
<div class="slot slot--tl">
  <section class="page cover">
    <div class="abs cover__frame"></div>
    <div class="abs cover__band"></div>
    <div class="photo photo--desk" style="left:91px;top:29px;width:373px;height:290px" role="img" aria-label="Photo of a person typing on a laptop at a desk with a plant"></div>
    <h1 class="abs cover__title">SOME TEXT HERE</h1>
    <p class="abs cover__subtitle">some text here</p>
    <div class="abs body-text" style="left:52px;top:436px;width:370px">
      <p>Lorem ipsum dolor sit amet, consectetuer adipiscing elit. Maecenas porttitor congue massa. Fusce posuere, magna sed pulvinar ultricies, purus lectus malesuada libero, sit amet commodo magna eros quis urna.</p>
      <p>Aenean nec lorem. In porttitor. Donec laoreet nonummy augue.</p>
      <p>Suspendisse dui purus, scelerisque at, vulputate vitae, pretium mattis, nunc. Mauris eget neque at sem venenatis eleifend. Ut nonummy.</p>
    </div>
    <div class="abs brand" style="left:52px;top:548px"><span class="brand__dot"></span>Bellwick</div>
    <div class="abs cover__bar"></div>
  </section>
</div>

<!-- Page 2 : inside left -->
<div class="slot slot--tr">
  <section class="page inside-a">
    <h2 class="abs header" style="left:29px;top:27px">Header Text</h2>
    <div class="abs body-text body-text--compact" style="left:35px;top:60px;width:212px">
      <p>Lorem ipsum dolor sit amet, consectetuer adipiscing elit. Maecenas porttitor congue massa. Fusce posuere, magna sed pulvinar ultricies, purus lectus malesuada libero, sit amet commodo magna eros quis urna. adipiscing elit. Maecenas porttitor congue massa. Fusce posuere, magna sed pulvinar ultricies, purus lectus malesuada libero, sit amet commodo magna eros quis urna.</p>
    </div>
    <div class="photo photo--coder" style="left:35px;top:172px;width:206px;height:204px" role="img" aria-label="Photo of hands typing on a laptop during a video call">
      <p class="photo__caption">Lorem ipsum dolor sit amet, consectetuer adipiscing elit. Maecenas porttitor</p>
    </div>
    <h3 class="abs teal-label side__title" style="left:267px;top:30px">LOREM IPSUM DOLOR SIT AMET</h3>
    <ul class="abs side__list" style="left:282px;top:50px">
      <li>Lorem Ipsum Dolor</li><li>Lorem Ipsum Dolor</li><li>Lorem Ipsum Dolor</li><li>Lorem Ipsum Dolor</li><li>Lorem Ipsum Dolor</li>
    </ul>
    <div class="abs side__box" style="left:274px;top:132px;width:192px;height:246px">
      <p>Lorem ipsum dolor sit amet, consectetuer adipiscing elit. Maecenas porttitor congue massa. Fusce posuere, magna sed pulvinar</p>
      <p>ultricies, purus lectus malesuada libero, sit amet commodo magna eros quis urna.</p>
      <p>adipiscing elit. Maecenas porttitor congue massa. Fusce posuere, magna sed pulvinar ultricies, purus lectus malesuada libero, sit amet commodo magna eros quis urna.</p>
      <p>Lorem ipsum dolor sit amet, consectetuer adipiscing elit. Maecenas porttitor congue massa. Fusce posuere, magna sed pulvinar ultricies, purus lectus malesuada libero, sit amet commodo magna eros quis urna.</p>
      <p>adipiscing elit. Maecenas porttitor congue massa. Fusce posuere, magna sed pulvinar ultricies, commodo magna eros quis urna.</p>
    </div>
    <h2 class="abs header" style="left:29px;top:392px">Header Text</h2>
    <div class="abs body-text body-text--compact" style="left:35px;top:422px;width:430px">
      <p>Lorem ipsum dolor sit amet, consectetuer adipiscing elit. Maecenas porttitor congue massa. Fusce posuere, magna sed pulvinar ultricies, purus lectus malesuada libero, sit amet commodo magna eros</p>
    </div>
    <figure class="thumb" style="left:37px;top:460px"><span class="teal-label thumb__label">Image 1</span><div class="photo--laptop thumb__img" role="img" aria-label="Photo of an open laptop"></div><figcaption class="thumb__caption">porttitor congue massa. Fusce sed malesuada libero,</figcaption></figure>
    <figure class="thumb" style="left:150px;top:460px"><span class="teal-label thumb__label">Image 2</span><div class="photo--laptop thumb__img" role="img" aria-label="Photo of an open laptop"></div><figcaption class="thumb__caption">porttitor congue massa. Fusce sed malesuada libero,</figcaption></figure>
    <figure class="thumb" style="left:262px;top:460px"><span class="teal-label thumb__label">Image 3</span><div class="photo--laptop thumb__img" role="img" aria-label="Photo of an open laptop"></div><figcaption class="thumb__caption">porttitor congue massa. Fusce sed malesuada libero,</figcaption></figure>
    <figure class="thumb" style="left:375px;top:460px"><span class="teal-label thumb__label">Image 4</span><div class="photo--laptop thumb__img" role="img" aria-label="Photo of an open laptop"></div><figcaption class="thumb__caption">porttitor congue massa. Fusce sed malesuada libero,</figcaption></figure>
    <div class="rule" style="left:35px;top:618px;width:425px"></div>
  </section>
</div>

<!-- Page 3 : inside right -->
<div class="slot slot--bl">
  <section class="page inside-b">
    <h2 class="abs header" style="left:29px;top:30px">Header Text</h2>
    <div class="abs body-text body-text--compact" style="left:34px;top:62px;width:168px">
      <p>Lorem ipsum dolor sit amet, consectetuer adipiscing elit. Maecenas porttitor congue massa. Fusce posuere, magna sed pulvinar ultricies, purus lectus malesuada libero, sit amet commodo magna eros quis urna. adipiscing elit. Maecenas porttitor congue massa. Fusce posuere, magna sed pulvinar ultricies, purus lectus malesuada libero, sit amet commodo magna eros quis urna.</p>
      <p>Lorem ipsum dolor sit amet, consectetuer adipiscing elit. Maecenas porttitor congue massa. Fusce posuere, magna sed pulvinar ultricies, purus lectus malesuada libero, sit amet commodo magna eros quis urna. adipiscing elit. Maecenas porttitor congue massa. Fusce posuere, magna</p>
    </div>
    <div class="photo photo--office" style="left:211px;top:30px;width:281px;height:255px" role="img" aria-label="Photo of a man working at a desktop computer in a bright office"></div>
    <div class="step" style="left:34px;top:312px"><div class="step__num">1</div><h4 class="teal-label step__head">Header Text</h4><p class="body-text">Lorem ipsum dolor sit amet, consectetuer adipiscing elit. Maecenas porttitor congue massa. Fusce posuere, magna sed pulvinar ultricies, purus lectus malesuada libero, sit amet commodo magna eros quis urna. adipiscing elit. Maecenas porttitor</p></div>
    <div class="step" style="left:260px;top:312px"><div class="step__num">2</div><h4 class="teal-label step__head">Header Text</h4><p class="body-text">Lorem ipsum dolor sit amet, consectetuer adipiscing elit. Maecenas porttitor congue massa. Fusce posuere, magna sed pulvinar ultricies, purus lectus malesuada libero, sit amet commodo magna eros quis urna. adipiscing elit. Maecenas porttitor</p></div>
    <div class="step" style="left:34px;top:462px"><div class="step__num">3</div><h4 class="teal-label step__head">Header Text</h4><p class="body-text">Lorem ipsum dolor sit amet, consectetuer adipiscing elit. Maecenas porttitor congue massa. Fusce posuere, magna sed pulvinar ultricies, purus lectus malesuada libero, sit amet commodo magna eros quis urna. adipiscing elit. Maecenas porttitor</p></div>
    <div class="step" style="left:260px;top:462px"><div class="step__num">4</div><h4 class="teal-label step__head">Header Text</h4><p class="body-text">Lorem ipsum dolor sit amet, consectetuer adipiscing elit. Maecenas porttitor congue massa. Fusce posuere, magna sed pulvinar ultricies, purus lectus malesuada libero, sit amet commodo magna eros quis urna. adipiscing elit. Maecenas porttitor</p></div>
    <div class="rule" style="left:28px;top:620px;width:435px"></div>
  </section>
</div>

<!-- Page 4 : back -->
<div class="slot slot--br">
  <section class="page back">
    <div class="photo photo--cafe" style="left:29px;top:30px;width:433px;height:290px" role="img" aria-label="Photo of a person holding a phone and coffee beside a laptop"></div>
    <div class="abs back__band"></div>
    <h2 class="abs back__title">SOME TEXT HERE</h2>
    <div class="abs body-text" style="left:34px;top:375px;width:190px">
      <p>Lorem ipsum dolor sit amet, consectetuer adipiscing elit. Maecenas porttitor congue massa. Fusce posuere, magna sed pulvinar ultricies, purus lectus malesuada libero, sit amet commodo magna eros quis urna.</p>
      <p style="margin-top:24px">Lorem ipsum dolor sit amet, consectetuer adipiscing elit. Maecenas porttitor congue massa. Fusce posuere, magna sed pulvinar ultricies, purus lectus malesuada libero, sit amet commodo magna eros quis urna.</p>
    </div>
    <div class="abs brand" style="left:34px;top:548px;font-size:30px"><span class="brand__dot" style="width:32px;height:32px"></span>Bellwick</div>
    <ul class="abs contact" style="left:314px;top:522px">
      <li><svg viewBox="0 0 10 10"><circle cx="5" cy="5" r="5" fill="#7a4208"/><path d="M3.2 2.6l1 1-.5.7a4 4 0 0 0 2 2l.7-.5 1 1-.6.7C5 7.4 2.6 5 2.6 3.2z" fill="#fff"/></svg>+123456789</li>
      <li><svg viewBox="0 0 10 10"><circle cx="5" cy="5" r="5" fill="#7a4208"/><rect x="2.6" y="3.2" width="4.8" height="3.6" fill="none" stroke="#fff" stroke-width=".8"/><path d="M2.6 3.2L5 5.2l2.4-2" fill="none" stroke="#fff" stroke-width=".8"/></svg>yourmail@mail.com</li>
      <li><svg viewBox="0 0 10 10"><circle cx="5" cy="5" r="5" fill="#7a4208"/><circle cx="5" cy="5" r="2.6" fill="none" stroke="#fff" stroke-width=".7"/><path d="M2.4 5h5.2M5 2.4v5.2" stroke="#fff" stroke-width=".6"/></svg>www.bellwick.com</li>
      <li><svg viewBox="0 0 10 10"><circle cx="5" cy="5" r="5" fill="#7a4208"/><path d="M5 8L3 5a2 2 0 1 1 4 0z" fill="#fff"/><circle cx="5" cy="4.6" r=".8" fill="#7a4208"/></svg>your address here</li>
    </ul>
  </section>
</div>

</body>
</html>
```